Building Company Business Card Design

I am looking to get a business card designed for my Building Company. Please find the logo attached.

Industry/Entity Type

Business

Contact Information for Business Card

Mobile 0472 913 046
Email admin@tarrowconstructworks.com.au
Website www.tarrowconstructworks.com.au

Colors
0255a3

```html
<!DOCTYPE html>
<html lang="en">
<head>
<meta charset="utf-8">
<title>Tarrow Construct Works – Business Card</title>
<link rel="stylesheet" href="https://fonts.googleapis.com/css2?family=Montserrat:wght@600&family=Open+Sans:wght@400&display=swap">
<style>
  :root {
    --backdrop: #001466;
    --card: #ffffff;
    --brand-blue: #0255a3;
    --slate: #5f6b73;
    --slate-soft: rgba(95, 107, 115, 0.12);
    --text: #4a4f54;
  }
  * { margin: 0; padding: 0; box-sizing: border-box; }
  html, body { width: 1200px; height: 534px; overflow: hidden; }
  body { background: var(--backdrop); position: relative; font-family: "Open Sans", sans-serif; }

  .card {
    position: absolute;
    top: 103px;
    width: 498px;
    height: 322px;
    background: var(--card);
    overflow: hidden;
    box-shadow: 0 8px 18px rgba(0, 0, 0, 0.35);
  }
  .card--back { left: 82px; }
  .card--front { left: 628px; }

  .brand {
    position: absolute;
    font-family: "Montserrat", sans-serif;
    font-weight: 600;
    color: var(--brand-blue);
    white-space: nowrap;
    line-height: 1.05;
  }
  .brand-line { display: flex; align-items: center; justify-content: flex-end; }
  .brand-rule { flex: 1; height: 2px; background: var(--slate); margin-right: 0.4em; }

  .card--back .brand { left: 89px; top: 90px; width: 184px; font-size: 17px; letter-spacing: 0.01em; }
  .card--front .brand { left: 109px; top: 142px; width: 291px; font-size: 27px; letter-spacing: 0.01em; }
  .card--front .brand-rule { height: 3px; }

  .skyline {
    position: absolute;
    background: linear-gradient(to top, var(--slate) 0%, var(--slate) 40%, var(--slate-soft) 100%);
  }
  .card--back .skyline { left: 76px; top: 173px; width: 154px; height: 26px; }
  .card--front .skyline { left: 125px; top: 275px; width: 282px; height: 45px; }

  .ground-line { position: absolute; height: 2px; background: var(--slate); }
  .card--back .ground-line { left: 0; top: 198px; width: 272px; }
  .card--front .ground-line { left: 0; top: 319px; width: 498px; height: 3px; }

  .contact-list { position: absolute; left: 88px; top: 236px; list-style: none; }
  .contact-item {
    display: flex;
    align-items: center;
    height: 20px;
    font-size: 15px;
    color: var(--text);
  }
  .contact-icon { width: 14px; height: 14px; margin-right: 11px; flex: none; }
</style>
</head>
<body>
  <section class="card card--back">
    <div class="brand">
      <div class="brand-line">TARROW CONSTRUCT</div>
      <div class="brand-line"><span class="brand-rule"></span>WORKS</div>
    </div>
    <div class="skyline" role="img" aria-label="City skyline silhouette"></div>
    <div class="ground-line"></div>
    <ul class="contact-list">
      <li class="contact-item">
        <svg class="contact-icon" viewBox="0 0 14 14" aria-hidden="true"><rect x="3.5" y="1" width="7" height="12" rx="1.2" fill="none" stroke="#0255a3" stroke-width="1.4"/><circle cx="7" cy="11" r="0.8" fill="#0255a3"/></svg>
        0472 913 046
      </li>
      <li class="contact-item">
        <svg class="contact-icon" viewBox="0 0 14 14" aria-hidden="true"><rect x="1" y="3" width="12" height="9" fill="#0255a3"/><path d="M1 3 L7 8 L13 3" fill="none" stroke="#fff" stroke-width="1.2"/></svg>
        admin@tarrowconstructworks.com.au
      </li>
      <li class="contact-item">
        <svg class="contact-icon" viewBox="0 0 14 14" aria-hidden="true"><circle cx="7" cy="7" r="5.8" fill="none" stroke="#0255a3" stroke-width="1.4"/><path d="M1.5 7 H12.5 M7 1.2 C4 4 4 10 7 12.8 M7 1.2 C10 4 10 10 7 12.8" fill="none" stroke="#0255a3" stroke-width="1"/></svg>
        www.tarrowconstructworks.com.au
      </li>
    </ul>
  </section>

  <section class="card card--front">
    <div class="brand">
      <div class="brand-line">TARROW CONSTRUCT</div>
      <div class="brand-line"><span class="brand-rule"></span>WORKS</div>
    </div>
    <div class="skyline" role="img" aria-label="City skyline silhouette"></div>
    <div class="ground-line"></div>
  </section>
</body>
</html>
```